Northern Falcon 250 Poster Design

Poster for the Public to draw them to the Event
- Northern Falcon 250. Largest Prize Money Race in Western Canada to Late Model Racing. Driver Competing for $65,000 in Prize Money Featuring Late Models and Street Stock Racers from Canada and the U.S. Don't miss the Inaugural Northern Falcon 250 at the Newly renovated Marlowe Raceway .
-Marlowe Raceway Address 1845 Quillan Road
- April 29th -30th
- Gates Open and 4:30 pm Racing starts at 5 pm
- Adults $20
- Youth 12-17 $15
- Senior $15
- Under 12 Free

This is a major event and the newly renovated Marlowe Raceway that will attract racers from many cities and Kick off the 2022 racing Season

Low design quality

Target Market(s)

Fans

Industry/Entity Type

Autombobile race

Requirements
Must have
• Dates, times, logo, address, cars
Nice to have
• Clear bold Dates, draws the eyes, cool car pictures of Asphalt Late Model Race Cars

```html
<!DOCTYPE html>
<html lang="en">
<head>
<meta charset="utf-8">
<title>Northern Falcon 250 – Event Poster</title>
<link rel="stylesheet" href="https://fonts.googleapis.com/css2?family=Anton&family=Bebas+Neue&family=Oswald:wght@500;700&display=swap">
<style>
  :root {
    --backdrop: #474747;
    --ink: #141414;
    --panel: #1b1b1b;
    --concrete: #d6d6d6;
    --concrete-dark: #c4c4c4;
    --yellow: #f0c51c;
    --white: #ffffff;
    --rule: #8a8a8a;
  }
  * { margin: 0; padding: 0; box-sizing: border-box; }
  html, body { width: 1004px; height: 1200px; overflow: hidden; background: var(--backdrop); }
  .poster {
    position: absolute; left: 106px; top: 40px;
    width: 792px; height: 1120px;
    background: var(--panel);
    overflow: hidden;
    font-family: "Bebas Neue", sans-serif;
    color: var(--white);
  }
  .header-band {
    position: absolute; left: 0; top: 0; width: 792px; height: 204px;
    background: linear-gradient(180deg, var(--concrete) 0%, var(--concrete-dark) 100%);
  }
  .event-mark {
    position: absolute; left: 44px; top: 58px; width: 250px;
    display: flex; align-items: center; gap: 12px;
  }
  .event-mark-dot { width: 40px; height: 40px; border-radius: 50%; background: var(--ink); flex: none; }
  .event-mark-name {
    font-family: "Oswald", sans-serif; font-weight: 700; font-size: 30px;
    line-height: 1.05; color: var(--ink); text-transform: uppercase;
  }
  .race-photo {
    position: absolute; left: 0; top: 204px; width: 792px; height: 408px;
    background: radial-gradient(ellipse at 55% 55%, #e8ecf2 0%, #8d97a8 35%, #4a4f58 70%, #2e3136 100%);
  }
  .prize-plate { position: absolute; left: 298px; top: 124px; width: 494px; height: 130px; }
  .prize-text {
    position: absolute; left: 330px; top: 128px; width: 444px; height: 106px;
    display: flex; align-items: center; justify-content: flex-end;
    font-size: 90px; line-height: 1; white-space: nowrap; letter-spacing: 1px;
  }
  .white-strip { position: absolute; left: 0; top: 612px; width: 792px; height: 13px; background: var(--white); }
  .info {
    position: absolute; left: 0; top: 625px; width: 792px; height: 495px;
    background: linear-gradient(180deg, var(--ink) 0%, var(--panel) 100%);
  }
  .date-badge { position: absolute; left: 156px; top: 576px; width: 480px; height: 90px; }
  .date-text {
    position: absolute; left: 156px; top: 576px; width: 480px; height: 90px;
    display: flex; align-items: center; justify-content: center;
    font-family: "Anton", sans-serif; font-size: 48px; line-height: 1;
    color: var(--ink); letter-spacing: 1px; white-space: nowrap;
  }
  .address-label {
    position: absolute; left: 0; top: 716px; width: 792px; text-align: center;
    font-family: "Oswald", sans-serif; font-weight: 500; font-size: 14px; letter-spacing: 9px;
  }
  .rule { position: absolute; height: 1px; background: var(--rule); }
  .address {
    position: absolute; left: 0; top: 750px; width: 792px; text-align: center;
    font-family: "Anton", sans-serif; font-size: 80px; line-height: 94px;
    letter-spacing: 2px; white-space: nowrap;
  }
  .schedule {
    position: absolute; left: 0; top: 866px; width: 792px;
    display: flex; justify-content: center; align-items: center;
    font-size: 36px; line-height: 40px; letter-spacing: 0.5px; white-space: nowrap;
  }
  .schedule-divider { width: 1px; height: 36px; background: var(--white); margin: 0 26px; }
  .tickets { position: absolute; left: 0; top: 950px; width: 792px; }
  .ticket { position: absolute; width: 114px; text-align: center; }
  .ticket-price { font-size: 66px; line-height: 70px; color: var(--yellow); border-bottom: 1px solid var(--rule); padding-bottom: 6px; }
  .ticket-type { font-size: 27px; line-height: 30px; margin-top: 10px; white-space: nowrap; }
</style>
</head>
<body>
  <main class="poster">
    <section class="header-band">
      <div class="event-mark">
        <span class="event-mark-dot"></span>
        <span class="event-mark-name">Northern Falcon 250</span>
      </div>
    </section>

    <div class="race-photo" role="img" aria-label="Photo of GT race cars cornering on a track, a white and blue car leading"></div>

    <svg class="prize-plate" viewBox="0 0 494 130" aria-hidden="true">
      <polygon points="28,0 494,0 494,106 0,106" fill="#1b1b1b"/>
      <rect x="228" y="106" width="266" height="24" fill="#f0c51c"/>
    </svg>
    <div class="prize-text">PRIZE: $65,000</div>

    <div class="white-strip"></div>

    <section class="info"></section>

    <svg class="date-badge" viewBox="0 0 480 90" aria-hidden="true">
      <polygon points="26,0 454,0 478,45 454,90 26,90 2,45" fill="#ffffff"/>
      <polygon points="32,5 448,5 470,45 448,85 32,85 10,45" fill="#f0c51c"/>
    </svg>
    <div class="date-text">APRIL 29TH - 30TH</div>

    <div class="address-label">MARLOWE RACEWAY ADDRESS</div>
    <div class="rule" style="left:160px; top:746px; width:472px;"></div>
    <div class="address">1845 QUILLAN ROAD</div>
    <div class="rule" style="left:76px; top:850px; width:640px; background:#bdbdbd;"></div>

    <div class="schedule">
      <span>Gates open at 4:30 PM</span>
      <span class="schedule-divider"></span>
      <span>Racing starts at 5 PM</span>
    </div>

    <div class="tickets">
      <div class="ticket" style="left:61px;"><div class="ticket-price">$20</div><div class="ticket-type">Adults</div></div>
      <div class="ticket" style="left:250px;"><div class="ticket-price">$15</div><div class="ticket-type">Youth 12-17</div></div>
      <div class="ticket" style="left:430px;"><div class="ticket-price">$15</div><div class="ticket-type">Senior</div></div>
      <div class="ticket" style="left:619px;"><div class="ticket-price">FREE</div><div class="ticket-type">Under 12</div></div>
    </div>

    <div class="rule" style="left:140px; top:1088px; width:512px; background:#3a3a3a;"></div>
  </main>
</body>
</html>
```